Real Estate Sign

My company is in need of a redesign for our real estate lawn sign. The sign should show our logo, the phrase "For Sale", our phone number 410-587-3391 and website www.HomeKeelTX.com.
Updates

Hello

Thank you for your submissions.  I am looking for the website and phone number to be very visible from a good distance.  I do also want to stay within the colors of my logo. Too many colors could be expensive to reproduce.

Thank you
Gordon

I favor clean, straight lines and design.  I prefer not to add any other graphics or logos on the sign.  The logo and name are enough. I am looking for readability from a good distance and prefer calls to action like call 410-593-3391 for information or visit www.HomeKeelTX.com to schedule tour today!  I don't really need FOR SALE to be so prominent.

thanks for all the submissions.
Gordon

Gordon

Industry/Entity Type

Real Estate

```html
<!DOCTYPE html>
<html lang="en">
<head>
<meta charset="utf-8">
<title>HomeKeel Realty – For Sale Sign</title>
<link rel="stylesheet" href="https://fonts.googleapis.com/css2?family=Open+Sans:wght@400;500&display=swap">
<style>
  :root {
    --sign-navy: #124274;
    --panel-navy: #113d6c;
    --accent-blue: #3aaee4;
    --ink-white: #ffffff;
    --frame-line: rgba(255, 255, 255, 0.85);
    --shadow: rgba(0, 0, 0, 0.55);
  }
  html, body {
    margin: 0;
    padding: 0;
    width: 1200px;
    height: 857px;
    overflow: hidden;
    background: var(--sign-navy);
  }
  .sign {
    position: relative;
    width: 1200px;
    height: 857px;
    background: var(--sign-navy);
    font-family: "Open Sans", Arial, sans-serif;
    color: var(--ink-white);
    overflow: hidden;
  }
  .sign__frame {
    position: absolute;
    inset: 10px;
    border: 1px solid var(--frame-line);
  }
  .brand-panel {
    position: absolute;
    left: 195px;
    top: 20px;
    width: 815px;
    height: 340px;
    background: var(--panel-navy);
    box-shadow: 4px 6px 10px var(--shadow);
    display: flex;
    align-items: center;
    justify-content: center;
  }
  .brand-panel__name {
    margin: 0;
    font-weight: 500;
    font-size: 104px;
    letter-spacing: 1px;
    color: var(--ink-white);
    white-space: nowrap;
  }
  .headline {
    position: absolute;
    left: 0;
    width: 1200px;
    top: 398px;
    margin: 0;
    text-align: center;
    font-weight: 400;
    font-size: 244px;
    line-height: 1;
    letter-spacing: -2px;
    text-shadow: 3px 4px 6px var(--shadow);
  }
  .headline__for { color: var(--accent-blue); }
  .headline__sale { color: var(--ink-white); }
  .headline-rule {
    position: absolute;
    left: 105px;
    top: 636px;
    width: 1000px;
    height: 2px;
    background: var(--ink-white);
  }
  .call-to-action {
    position: absolute;
    left: 0;
    width: 1170px;
    top: 712px;
    margin: 0;
    text-align: center;
    font-size: 40px;
    line-height: 60px;
    font-weight: 400;
    text-shadow: 2px 3px 4px var(--shadow);
  }
</style>
</head>
<body>
  <main class="sign">
    <div class="sign__frame"></div>

    <header class="brand-panel">
      <p class="brand-panel__name">HomeKeel Realty</p>
    </header>

    <h1 class="headline">
      <span class="headline__for">FOR</span> <span class="headline__sale">SALE</span>
    </h1>
    <div class="headline-rule"></div>

    <p class="call-to-action">
      call 410-593-3391 for information<br>
      or visit www.HomeKeelTX.com to schedule tour today
    </p>
  </main>
</body>
</html>
```